Women's Health Company needs business card

We need a business card for a USA based women's health care company. We use digital technology to enhance therapy prescribed by clinicians for their patients

```html
<!DOCTYPE html>
<html lang="en">
<head>
<meta charset="utf-8">
<title>Lumira Health – Business Card</title>
<link href="https://fonts.googleapis.com/css2?family=Roboto:wght@400;500;700&display=swap" rel="stylesheet">
<style>
  :root {
    --purple: #8e52a1;
    --teal: #6bbfba;
    --ink: #2b2b2b;
    --white: #ffffff;
    --backdrop: #e9e9ec;
  }
  * { box-sizing: border-box; margin: 0; padding: 0; }
  html, body {
    width: 1200px;
    height: 900px;
    overflow: hidden;
    background: var(--backdrop);
    font-family: "Roboto", Arial, sans-serif;
  }
  .canvas {
    width: 1200px;
    height: 900px;
    display: flex;
    align-items: center;
    justify-content: center;
    gap: 40px;
  }
  .card {
    width: 540px;
    height: 309px;
    position: relative;
    overflow: hidden;
    box-shadow: 0 6px 18px rgba(0,0,0,0.12);
  }

  /* Front */
  .card-front {
    background: var(--purple);
    display: flex;
    align-items: center;
    justify-content: center;
  }
  .brand {
    display: flex;
    align-items: center;
    gap: 12px;
    color: var(--teal);
    font-weight: 500;
  }
  .brand-dot {
    border-radius: 50%;
    background: var(--teal);
    flex: none;
  }
  .card-front .brand { font-size: 46px; }
  .card-front .brand-dot { width: 16px; height: 16px; }

  /* Back */
  .card-back { background: var(--white); }
  .card-back .brand {
    position: absolute;
    top: 58px;
    left: 150px;
    font-size: 32px;
    gap: 9px;
  }
  .card-back .brand-dot { width: 11px; height: 11px; }

  .person {
    position: absolute;
    left: 40px;
    top: 142px;
    width: 200px;
    text-align: right;
  }
  .person-name {
    color: var(--purple);
    font-weight: 700;
    font-size: 19px;
    letter-spacing: 0.3px;
  }
  .person-role {
    color: var(--ink);
    font-size: 13px;
    margin-top: 3px;
  }
  .divider {
    position: absolute;
    left: 256px;
    top: 128px;
    width: 1px;
    height: 76px;
    background: var(--purple);
  }
  .contact-list {
    position: absolute;
    left: 272px;
    top: 126px;
    list-style: none;
  }
  .contact-list li {
    display: flex;
    align-items: center;
    gap: 8px;
    font-size: 13px;
    color: var(--ink);
    line-height: 20px;
  }
  .contact-list svg { width: 12px; height: 12px; flex: none; }

  .address-band {
    position: absolute;
    left: 0;
    right: 0;
    top: 222px;
    height: 50px;
    background: var(--purple);
    color: var(--white);
    font-size: 15px;
    display: flex;
    align-items: center;
    justify-content: center;
    letter-spacing: 0.2px;
  }
</style>
</head>
<body>
<main class="canvas">

  <section class="card card-front" aria-label="Card front">
    <div class="brand"><span class="brand-dot"></span><span class="brand-name">Lumira Health</span></div>
  </section>

  <section class="card card-back" aria-label="Card back">
    <div class="brand"><span class="brand-dot"></span><span class="brand-name">Lumira Health</span></div>

    <div class="person">
      <p class="person-name">DANA WHITFIELD</p>
      <p class="person-role">CEO/Founder</p>
    </div>

    <div class="divider"></div>

    <ul class="contact-list">
      <li>
        <svg viewBox="0 0 12 12"><path fill="#6bbfba" d="M2.4 0.8l1.8 0 0.8 2.6-1.2 0.9c0.6 1.4 1.5 2.3 2.9 2.9l0.9-1.2 2.6 0.8 0 1.8c0 0.6-0.5 1.1-1.1 1.1C4.6 9.7 0.5 5.6 0.5 1.9c0-0.6 0.5-1.1 1.1-1.1z"/></svg>
        (555) 210-4836
      </li>
      <li>
        <svg viewBox="0 0 12 12"><rect x="3" y="0.8" width="6" height="10.4" rx="1" fill="none" stroke="#6bbfba" stroke-width="1.2"/><circle cx="6" cy="9.4" r="0.7" fill="#6bbfba"/></svg>
        (555) 374-9152
      </li>
      <li>
        <svg viewBox="0 0 12 12"><rect x="0.8" y="2.2" width="10.4" height="7.6" fill="#6bbfba"/><path d="M0.8 2.4l5.2 4 5.2-4" fill="none" stroke="#fff" stroke-width="1"/></svg>
        info@lumirahealth.com
      </li>
      <li>
        <svg viewBox="0 0 12 12"><circle cx="6" cy="6" r="5.2" fill="#6bbfba"/><path d="M1 6h10M6 0.8c-2 2.8-2 7.6 0 10.4M6 0.8c2 2.8 2 7.6 0 10.4" fill="none" stroke="#fff" stroke-width="0.8"/></svg>
        www.lumirahealth.com
      </li>
    </ul>

    <div class="address-band">PO Box 4120 Harbor Lane Springfield ST 6021</div>
  </section>

</main>
</body>
</html>
```